Boutique Film/TV Company needs Business Card Design

Please see our website for background on our company and look of our current logo: www.lumarocpictures.ca

Pantone 314U is our main colour.

Target Market(s)

Network of peers, funders and broadcasters.

Industry/Entity Type

Business

Requirements
Must have
• We would like rounded corners and the height of the card to be shorter than traditional (maybe?!)

It's important that we have room for our office address, office number, cell number, email address, website, facebook and linked-in info (though not all of us have a linked-in account).

Would like the logo to keep the exclamation marks over the letters but the tag line/tag words of "film - television - interactive" can stay or go or... surprise me!

Nice to have
• Silky matte finish.

We are open to a change in the font of our logo/name.

```html
<!DOCTYPE html>
<html lang="en">
<head>
<meta charset="utf-8">
<title>Lumaroc Business Card</title>
<link href="https://fonts.googleapis.com/css2?family=Source+Sans+3:ital,wght@0,400;0,600;0,700;1,700&display=swap" rel="stylesheet">
<style>
  :root {
    --brand-blue: #0a85ac;
    --ink: #111111;
    --text-grey: #333333;
    --accent-red: #9b1b1f;
    --paper: #ffffff;
    --backdrop: #e9e9e9;
    --social-grey: #8a8f94;
  }
  * { margin: 0; padding: 0; box-sizing: border-box; }
  html, body {
    width: 960px; height: 1200px; overflow: hidden;
    background: var(--backdrop);
    font-family: "Source Sans 3", sans-serif;
  }
  .canvas { position: relative; width: 960px; height: 1200px; }

  .card {
    position: absolute;
    width: 840px; height: 480px;
    border-radius: 28px;
    overflow: hidden;
  }
  .card-front { left: 60px; top: 88px; background: var(--paper); }
  .card-back { left: 55px; top: 638px; background: var(--brand-blue); }

  .header-wave { position: absolute; left: 0; top: 0; width: 840px; height: 180px; }

  .holder { position: absolute; right: 48px; top: 40px; text-align: right; color: var(--paper); }
  .holder-name { font-size: 36px; font-weight: 700; line-height: 1.1; }
  .holder-title { font-size: 27px; font-weight: 400; line-height: 1.2; }

  .brand-name {
    position: absolute;
    font-weight: 600;
    letter-spacing: 1px;
    line-height: 1;
  }
  .card-front .brand-name { left: 56px; top: 196px; font-size: 96px; color: var(--ink); }
  .card-back .brand-name { left: 0; width: 840px; text-align: center; top: 136px; font-size: 118px; color: var(--paper); }

  .tagline { position: absolute; font-weight: 700; white-space: nowrap; }
  .card-front .tagline { left: 56px; top: 308px; font-size: 21px; color: var(--accent-red); }
  .card-back .tagline { left: 0; width: 840px; text-align: center; top: 298px; font-size: 25px; color: var(--paper); }

  .follow { position: absolute; left: 60px; top: 398px; display: flex; align-items: center; gap: 10px; }
  .follow-label { font-size: 28px; font-weight: 700; color: var(--text-grey); margin-right: 2px; }
  .social-square { width: 36px; height: 36px; border-radius: 3px; background: var(--social-grey); }

  .contact {
    position: absolute; right: 40px; top: 230px;
    text-align: right; color: var(--text-grey);
    font-size: 23px; line-height: 32px;
  }
  .contact-group + .contact-group { margin-top: 11px; }
  .contact-label { font-weight: 700; font-style: italic; }
</style>
</head>
<body>
<main class="canvas">
  <section class="card card-front">
    <svg class="header-wave" viewBox="0 0 840 180" aria-hidden="true">
      <path d="M0 78 C130 60 280 70 420 110 C560 150 720 150 840 134 L840 142 C700 166 540 172 400 152 C260 128 120 118 0 128 Z" fill="var(--ink)"/>
      <path d="M0 0 H840 V128 C700 142 560 140 420 100 C280 60 120 52 0 66 Z" fill="var(--brand-blue)"/>
    </svg>
    <div class="holder">
      <div class="holder-name">Your Name</div>
      <div class="holder-title">Designation</div>
    </div>
    <div class="brand-name">Lumaroc</div>
    <div class="tagline">Films • Television • Interactive</div>
    <div class="follow">
      <span class="follow-label">Follow</span>
      <span class="social-square"></span>
      <span class="social-square"></span>
    </div>
    <div class="contact">
      <div class="contact-group">
        <div><span class="contact-label">t</span> : 416.555.0182</div>
        <div><span class="contact-label">c</span> : 647.555.0147</div>
      </div>
      <div class="contact-group">
        <div><span class="contact-label">e</span> : info@lumarocpictures.ca</div>
        <div><span class="contact-label">w</span> : www.lumarocpictures.ca</div>
      </div>
      <div class="contact-group">
        <div>42 Alder Lane</div>
        <div>Toronto, ON M4E 2K9</div>
      </div>
    </div>
  </section>

  <section class="card card-back">
    <div class="brand-name">Lumaroc</div>
    <div class="tagline">Films • Television • Interactive</div>
  </section>
</main>
</body>
</html>
```